Business card design needed

We need a business card design for a new micro business based in Melbourne (Australia). Our main service is cleaning and fixing Vertical Blinds as a cheaper alternative than buying new blinds. A smaller part of the business is fitting affordable & temporary alternatives to double glazed windows both for noise abatement and climate control and reduction in energy costs.
We could be dealing with commercial as well as residential customers so we need a quality look. The design needs to reflect our core business of vertical blinds cleaning & maintenance.

Target Market(s)

Not sure yet. These Business Cards are going to be used to test the market

Industry/Entity Type

Residential

Contact Information for Business Card

Teloria Brinkhaus. Vertical Blinds Cleaning, Maintenance & Temporary Window Insulation Solutions. Ph: 03 9274 5163. Mob: 0497 362 514.

```html
<!DOCTYPE html>
<html lang="en">
<head>
<meta charset="utf-8">
<title>Teloria Brinkhaus – Business Card Options</title>
<link rel="stylesheet" href="https://fonts.googleapis.com/css2?family=Alfa+Slab+One&family=Archivo+Black&family=Roboto:wght@400&display=swap">
<style>
  :root {
    --board: #eeeeee;
    --charcoal: #2c2a29;
    --orange: #f0831f;
    --white: #ffffff;
    --label: #333333;
    --text-shadow: rgba(0,0,0,0.25);
  }
  html, body {
    margin: 0;
    padding: 0;
    width: 1110px;
    height: 1200px;
    overflow: hidden;
    background: var(--board);
  }
  .board {
    position: relative;
    width: 1110px;
    height: 1200px;
  }
  .option-number {
    position: absolute;
    font-family: "Roboto", Arial, sans-serif;
    font-size: 34px;
    color: var(--label);
  }
  .card {
    position: absolute;
    background: var(--white);
    border-radius: 42px;
    overflow: hidden;
    box-shadow: 0 6px 14px rgba(0,0,0,0.28);
  }
  .card--one { left: 106px; top: 85px; width: 867px; height: 497px; }
  .card--two { left: 114px; top: 616px; width: 864px; height: 501px; }

  .card__band {
    position: absolute;
    left: 0; top: 0; right: 0;
    background: var(--charcoal);
    border-bottom: 16px solid var(--orange);
  }
  .card--one .card__band { height: 265px; }
  .card--two .card__band { height: 269px; }

  .card__artwork {
    position: absolute;
    bottom: 0;
  }
  .card--one .card__artwork {
    left: 24px; width: 346px; height: 242px;
    background: linear-gradient(90deg, #f0831f 0%, #d9741a 45%, #3a2f27 100%);
  }
  .card--two .card__artwork {
    left: 23px; width: 347px; height: 249px;
    background: linear-gradient(90deg, #ffffff 0%, #f6b575 50%, #f0831f 100%);
  }

  .card__name {
    position: absolute;
    margin: 0;
    font-family: "Alfa Slab One", Georgia, serif;
    font-weight: 400;
    color: var(--white);
    white-space: nowrap;
  }
  .card--one .card__name { left: 448px; top: 40px; font-size: 33px; }
  .card--two .card__name { left: 465px; top: 72px; font-size: 28px; }

  .contact {
    position: absolute;
    margin: 0;
    padding: 0;
    list-style: none;
    font-family: "Archivo Black", Arial, sans-serif;
    color: var(--white);
  }
  .contact__item {
    display: flex;
    align-items: center;
    white-space: nowrap;
  }
  .contact__icon { fill: var(--white); flex: none; }
  .card--one .contact { left: 490px; top: 120px; font-size: 29px; }
  .card--one .contact__item { height: 52px; gap: 16px; }
  .card--one .contact__icon { width: 26px; height: 30px; }
  .card--two .contact { left: 510px; top: 130px; font-size: 25px; }
  .card--two .contact__item { height: 44px; gap: 14px; }
  .card--two .contact__icon { width: 22px; height: 26px; }

  .card__tagline {
    position: absolute;
    margin: 0;
    font-family: "Alfa Slab One", Georgia, serif;
    font-weight: 400;
    color: var(--orange);
    text-shadow: 1px 2px 2px var(--text-shadow);
    text-align: justify;
    text-align-last: justify;
  }
  .card__tagline span { display: block; }
  .card--one .card__tagline { left: 60px; width: 752px; top: 318px; font-size: 29.5px; line-height: 52px; }
  .card--two .card__tagline { left: 56px; width: 764px; top: 347px; font-size: 29px; line-height: 49px; }
</style>
</head>
<body>
<main class="board">

  <span class="option-number" style="left:40px; top:114px;">1</span>
  <article class="card card--one">
    <div class="card__band">
      <div class="card__artwork" role="img" aria-label="Illustration area: silhouette of a worker cleaning vertical blinds, orange slats on charcoal"></div>
      <h1 class="card__name">Teloria Brinkhaus</h1>
      <ul class="contact">
        <li class="contact__item">
          <svg class="contact__icon" viewBox="0 0 24 24" aria-hidden="true"><path d="M6.6 10.8a15.1 15.1 0 0 0 6.6 6.6l2.2-2.2a1 1 0 0 1 1-.25 11.4 11.4 0 0 0 3.6.57 1 1 0 0 1 1 1V20a1 1 0 0 1-1 1A17 17 0 0 1 3 4a1 1 0 0 1 1-1h3.5a1 1 0 0 1 1 1c0 1.25.2 2.45.57 3.57a1 1 0 0 1-.25 1z"/></svg>
          <span>03 9274 5163</span>
        </li>
        <li class="contact__item">
          <svg class="contact__icon" viewBox="0 0 24 24" aria-hidden="true"><path d="M7 1h10a2 2 0 0 1 2 2v18a2 2 0 0 1-2 2H7a2 2 0 0 1-2-2V3a2 2 0 0 1 2-2zm0 3v13h10V4zm5 15a1 1 0 1 0 0 2 1 1 0 0 0 0-2z"/></svg>
          <span>0497 362 514</span>
        </li>
      </ul>
    </div>
    <p class="card__tagline">
      <span>Vertical Blinds Cleaning, Maintenance</span>
      <span>&amp; Temporary Window Insulation Solutions</span>
    </p>
  </article>

  <span class="option-number" style="left:50px; top:650px;">2</span>
  <article class="card card--two">
    <div class="card__band">
      <div class="card__artwork" role="img" aria-label="Illustration area: orange silhouette of a worker cleaning white vertical blinds"></div>
      <h2 class="card__name">Teloria Brinkhaus</h2>
      <ul class="contact">
        <li class="contact__item">
          <svg class="contact__icon" viewBox="0 0 24 24" aria-hidden="true"><path d="M6.6 10.8a15.1 15.1 0 0 0 6.6 6.6l2.2-2.2a1 1 0 0 1 1-.25 11.4 11.4 0 0 0 3.6.57 1 1 0 0 1 1 1V20a1 1 0 0 1-1 1A17 17 0 0 1 3 4a1 1 0 0 1 1-1h3.5a1 1 0 0 1 1 1c0 1.25.2 2.45.57 3.57a1 1 0 0 1-.25 1z"/></svg>
          <span>03 9274 5163</span>
        </li>
        <li class="contact__item">
          <svg class="contact__icon" viewBox="0 0 24 24" aria-hidden="true"><path d="M7 1h10a2 2 0 0 1 2 2v18a2 2 0 0 1-2 2H7a2 2 0 0 1-2-2V3a2 2 0 0 1 2-2zm0 3v13h10V4zm5 15a1 1 0 1 0 0 2 1 1 0 0 0 0-2z"/></svg>
          <span>0497 362 514</span>
        </li>
      </ul>
    </div>
    <p class="card__tagline">
      <span>Vertical Blinds Cleaning, Maintenance</span>
      <span>&amp; Temporary Window Insulation Solutions</span>
    </p>
  </article>

</main>
</body>
</html>
```